Poster for pawn shop lobby

Looking for green and gold as my colors, like the picture shown of my old poster. This time I'm contemplating with doing pictures as well as just text. Here are ideas of things I buy and give loans on. We want to emphasize jewelry, laptops, game systems, tools. I'm open-minded.
Old & Broken Gold
Jewelry & Collectibles
Diamonds
Video Games & Systems
Up-to-date Computers & Laptops
Tablets
Cameras
Power Tools
Home & Garden Equipment
Sports Equipment
Watches
Antique Collectibles
Musical Instruments
And anything else of value

```html
<!DOCTYPE html>
<html lang="en">
<head>
<meta charset="utf-8">
<title>Pawn Shop Lobby Poster</title>
<link href="https://fonts.googleapis.com/css2?family=Open+Sans:wght@700;800&display=swap" rel="stylesheet">
<style>
  :root {
    --green: #8cc63f;
    --green-deep: #3d6b1e;
    --green-faint: #7ab536;
    --gold: #fbe918;
    --header-top: #fff03a;
    --header-bottom: #fdb813;
    --ink: #111111;
    --white: #ffffff;
  }
  html, body { margin: 0; padding: 0; overflow: hidden; }
  body { width: 848px; height: 1200px; font-family: "Open Sans", Arial, sans-serif; }
  .poster {
    position: relative; width: 848px; height: 1200px; overflow: hidden;
    background: var(--green);
  }
  .masthead {
    position: absolute; left: 0; top: 0; width: 848px; height: 162px;
    background: linear-gradient(90deg, var(--header-top) 0%, #ffd92a 55%, var(--header-bottom) 100%);
  }
  .masthead svg { position: absolute; left: 0; top: 0; }
  .dollar {
    position: absolute; font-weight: 800; color: var(--green-faint);
    line-height: 1; pointer-events: none;
  }
  .heading {
    position: absolute; margin: 0; font-size: 23px; font-weight: 700;
    color: var(--gold); line-height: 1; white-space: nowrap;
  }
  .rule { position: absolute; height: 4px; background: var(--gold); }
  .items {
    position: absolute; margin: 0; padding: 0; list-style: none;
    font-size: 19px; font-weight: 700; color: var(--ink); line-height: 26px;
    white-space: nowrap;
  }
  .items.right { text-align: right; }
  .photo-disc {
    position: absolute; border-radius: 50%; border: 5px solid var(--green-deep);
    box-sizing: border-box; background: radial-gradient(circle, #ffffff 55%, #e4e4e4 100%);
  }
  .photo-panel {
    position: absolute; border-radius: 16px; border: 5px solid var(--green-deep);
    box-sizing: border-box; background: linear-gradient(180deg, #ffffff 0%, #ececec 100%);
  }
</style>
</head>
<body>
<main class="poster">

  <header class="masthead">
    <svg width="848" height="162" viewBox="0 0 848 162">
      <text x="18" y="150" textLength="588" lengthAdjust="spacingAndGlyphs"
            font-family="Open Sans, Arial, sans-serif" font-weight="800" font-size="162" fill="#111111">PAWN SH</text>
      <circle cx="657" cy="88" r="60" fill="#d9c7b4" stroke="#3d6b1e" stroke-width="10"/>
      <text x="711" y="150" textLength="127" lengthAdjust="spacingAndGlyphs"
            font-family="Open Sans, Arial, sans-serif" font-weight="800" font-size="162" fill="#111111">P</text>
    </svg>
    <div role="img" aria-label="Shop owner holding a fan of banknotes"
         style="position:absolute;left:602px;top:33px;width:110px;height:110px;border-radius:50%;background:radial-gradient(circle at 50% 40%,#c9b7a6 0%,#b88a70 60%,#a0604c 100%);"></div>
  </header>

  <span class="dollar" style="left:370px;top:170px;font-size:300px;">$</span>
  <span class="dollar" style="left:462px;top:600px;font-size:170px;">$</span>
  <span class="dollar" style="left:335px;top:870px;font-size:200px;">$</span>

  <!-- Audio & Video -->
  <h2 class="heading" style="left:35px;top:200px;">AUDIO &amp; VIDEO</h2>
  <div class="rule" style="left:32px;top:234px;width:226px;"></div>
  <ul class="items" style="left:37px;top:257px;">
    <li>Car Audio</li>
    <li>Home Audio Systems</li>
    <li>Speakers</li>
    <li>Televisions</li>
    <li>Home Theater Systems</li>
    <li>Functioning Electronic Devices</li>
  </ul>
  <div class="photo-disc" role="img" aria-label="Pair of black studio speakers"
       style="left:262px;top:172px;width:148px;height:148px;background:radial-gradient(circle,#3a3a3a 0%,#2a2a2a 35%,#ffffff 60%);"></div>

  <div class="photo-panel" role="img" aria-label="Kitchen appliances and a vacuum cleaner"
       style="left:533px;top:188px;width:293px;height:186px;"></div>

  <!-- Musical Instruments -->
  <h2 class="heading" style="right:26px;top:404px;">MUSICAL INSTRUMENTS</h2>
  <div class="rule" style="left:518px;top:439px;width:304px;"></div>
  <div class="photo-disc" role="img" aria-label="Small acoustic guitar"
       style="left:451px;top:443px;width:118px;height:118px;background:radial-gradient(circle,#f3dfb8 0%,#fafafa 55%);"></div>
  <ul class="items right" style="right:35px;top:477px;">
    <li>Guitars</li>
    <li>Band Instruments</li>
    <li>Amplifiers</li>
    <li>DJ Equipment</li>
  </ul>

  <!-- DVD & Blu-ray -->
  <h2 class="heading" style="left:28px;top:445px;">DVD &amp; BLU-RAY MOVIES</h2>
  <div class="rule" style="left:28px;top:477px;width:368px;"></div>
  <ul class="items" style="left:30px;top:498px;">
    <li>DVD Movies</li>
    <li>Blu-Ray Movies</li>
  </ul>

  <!-- Sporting -->
  <h2 class="heading" style="left:25px;top:573px;">SPORTING EQUIPMENT &amp; VEHICLES</h2>
  <div class="rule" style="left:25px;top:607px;width:441px;"></div>
  <ul class="items" style="left:35px;top:632px;">
    <li>Sports Equipment</li>
    <li>Motorcycles</li>
    <li>Snowmobiles</li>
    <li>Golf Clubs</li>
    <li>Bicycles</li>
  </ul>
  <div class="photo-disc" role="img" aria-label="Golf bag with clubs"
       style="left:257px;top:622px;width:148px;height:148px;background:radial-gradient(circle,#7a3a4a 0%,#b9b9b9 45%,#ffffff 70%);"></div>

  <!-- Miscellaneous -->
  <h2 class="heading" style="right:26px;top:595px;">MISCELLANEOUS</h2>
  <div class="rule" style="left:575px;top:628px;width:247px;"></div>
  <ul class="items right" style="right:39px;top:637px;">
    <li>Microwave Ovens</li>
    <li>Small Home Appliances</li>
    <li>Quality Leather</li>
    <li>Artwork</li>
  </ul>

  <!-- Video Games & Computers -->
  <h2 class="heading" style="left:35px;top:788px;">VIDEO GAMES &amp; COMPUTERS</h2>
  <div class="rule" style="left:28px;top:821px;width:398px;"></div>
  <ul class="items" style="left:33px;top:846px;">
    <li>Video Games &amp; Systems</li>
    <li>Up-to-date Computers &amp; Laptops</li>
    <li>Tablets</li>
    <li>Monitors &amp; Accessories</li>
    <li>Compact Discs</li>
  </ul>
  <div class="photo-disc" role="img" aria-label="Handheld game console controller"
       style="left:373px;top:815px;width:118px;height:118px;background:radial-gradient(circle,#2b2b2b 0%,#3a3a3a 40%,#ffffff 62%);"></div>

  <!-- Jewelry -->
  <h2 class="heading" style="right:26px;top:791px;">JEWELRY &amp; COLLECTIBLES</h2>
  <div class="rule" style="left:492px;top:825px;width:330px;"></div>
  <ul class="items right" style="right:33px;top:844px;">
    <li>Diamond &amp; Gemstone Jewelry</li>
    <li>Watches</li>
    <li>Old &amp; Broken Gold</li>
    <li>Antique Collectibles</li>
  </ul>

  <div class="photo-panel" role="img" aria-label="Laptop, tablet and smartphone"
       style="left:25px;top:995px;width:292px;height:186px;background:linear-gradient(160deg,#ffffff 0%,#5aa6e6 45%,#1f5fae 75%,#e8e8e8 100%);"></div>

  <div class="photo-disc" role="img" aria-label="Assortment of hand and power tools"
       style="left:347px;top:992px;width:178px;height:178px;background:radial-gradient(circle,#9a9a9a 0%,#c7a35c 40%,#d9d9d9 75%,#ffffff 100%);"></div>

  <!-- Home Improvement -->
  <h2 class="heading" style="right:26px;top:987px;">HOME IMPROVEMENT</h2>
  <div class="rule" style="left:548px;top:1020px;width:274px;"></div>
  <ul class="items right" style="right:38px;top:1035px;">
    <li>Power Tools</li>
    <li>Home &amp; Garden Equipment</li>
    <li>Lawn Mowers</li>
    <li>Leaf Blowers</li>
    <li>Snow Blowers</li>
  </ul>

</main>
</body>
</html>
```